A4 Flyer

Bright Path Learning is starting a course in regional Victoria. We are currently advertising (See attached file A34984) in local papers but need to create a one page flyer to distribute to Aged Care facilities in the area. The A4 flyer will be inserted into a folder pack with more detailed information on Bright Path Learning. Important to use images and logoes attached

Target Market(s)

Flyer to be distributed to Aged Care facility staff and owners

Industry/Entity Type

Advertising

Font styles to use
Sans Serif

Colors
f37123
ec1f27

Requirements
Must have
• BPL Logo
Some image

```html
<!DOCTYPE html>
<html lang="en">
<head>
<meta charset="utf-8">
<title>Bright Path Learning – Fast Track Course Flyer</title>
<link href="https://fonts.googleapis.com/css2?family=Fira+Sans+Condensed:wght@400;500;600;700;800&family=Fira+Sans:wght@300;400;700&display=swap" rel="stylesheet">
<style>
  :root {
    --orange: #f37123;
    --red: #ec1f27;
    --banner-red: #e2483a;
    --deep-orange: #f58b3c;
    --ink: #1a1a1a;
    --slate: #4d4d4f;
    --white: #ffffff;
    --photo-warm: #d9d2cc;
    --photo-cool: #c9d6e0;
  }
  * { margin: 0; padding: 0; box-sizing: border-box; }
  html, body { width: 848px; height: 1200px; overflow: hidden; }
  body {
    position: relative;
    background: radial-gradient(ellipse at 30% 20%, #f7862f 0%, var(--orange) 45%, #e5452a 100%);
    font-family: "Fira Sans Condensed", "Arial Narrow", sans-serif;
    color: var(--ink);
  }
  .sheet {
    position: absolute; left: 45px; top: 45px; width: 760px; height: 1110px;
    background: var(--white); border-radius: 30px;
  }
  .banner {
    position: absolute; left: 75px; top: 74px; width: 692px; height: 132px;
    border-radius: 16px;
    background: linear-gradient(90deg, var(--banner-red) 0%, #ea5a34 55%, var(--orange) 100%);
    text-align: center; color: var(--white); font-weight: 700;
    text-shadow: 3px 3px 0 #3a1d14;
  }
  .banner__title { font-size: 41px; line-height: 1; padding-top: 15px; }
  .banner__sub { font-size: 33px; line-height: 1; margin-top: 16px; }
  .photo { position: absolute; left: 78px; width: 309px; }
  .photo--student { top: 238px; height: 352px; background: linear-gradient(160deg, #eef0f2 0%, var(--photo-warm) 45%, #3a3330 100%); }
  .photo--trainer { top: 604px; height: 351px; background: linear-gradient(160deg, #f3f4f6 0%, var(--photo-cool) 50%, #c8897a 100%); }
  .venue { position: absolute; left: 514px; top: 214px; width: 262px; height: 172px; }
  .venue svg { position: absolute; inset: 0; }
  .venue__text {
    position: absolute; inset: 0; display: flex; flex-direction: column;
    justify-content: center; align-items: center; text-align: center;
    font-size: 22px; font-weight: 500; line-height: 1.4; padding-top: 4px;
  }
  .headline {
    position: absolute; left: 407px; top: 414px; width: 385px;
    color: var(--red); font-size: 28px; font-weight: 700; line-height: 1.17;
    text-transform: uppercase; letter-spacing: 0.2px;
  }
  .funding { position: absolute; left: 407px; top: 538px; font-size: 15.5px; line-height: 1.3; font-family: "Fira Sans", sans-serif; }
  .enrol { position: absolute; left: 407px; top: 612px; width: 380px; }
  .enrol__label { color: var(--red); font-size: 24px; font-weight: 500; }
  .enrol__web { color: var(--slate); font-size: 32px; font-weight: 700; margin-top: 6px; line-height: 1.1; white-space: nowrap; }
  .enrol__phone { color: var(--red); font-size: 34px; font-weight: 700; line-height: 1.2; }
  .modules {
    position: absolute; left: 408px; top: 775px; width: 359px; height: 353px;
    border: 1.5px solid var(--red); border-radius: 20px; padding: 6px;
  }
  .modules__inner {
    width: 100%; height: 100%; background: var(--deep-orange); border-radius: 14px;
    padding: 14px 18px;
  }
  .modules__intro { text-align: center; font-size: 16.5px; line-height: 1.3; }
  .modules__list { list-style: none; margin: 16px 0 0 48px; }
  .modules__list li { display: flex; align-items: center; font-size: 17.5px; height: 30.5px; }
  .modules__list svg { width: 14px; height: 14px; margin-right: 24px; }
  .brand {
    position: absolute; left: 76px; top: 1090px;
    display: flex; align-items: center; gap: 10px;
    color: var(--orange); font-size: 30px; font-weight: 500; line-height: 1;
  }
  .brand__dot { width: 18px; height: 18px; border-radius: 50%; background: var(--orange); }
  .toid { position: absolute; left: 306px; top: 1118px; font-family: "Times New Roman", serif; font-size: 14px; }
</style>
</head>
<body>
  <div class="sheet"></div>

  <header class="banner">
    <div class="banner__title">Unique Opportunity!</div>
    <div class="banner__sub">Fast Track Course - Start July 2014</div>
  </header>

  <div class="photo photo--student" role="img" aria-label="Photo of a smiling student seated at a desk in a classroom"></div>
  <div class="photo photo--trainer" role="img" aria-label="Photo of a trainer pointing at an anatomical torso model"></div>

  <div class="venue">
    <svg viewBox="0 0 262 168" preserveAspectRatio="none" aria-hidden="true">
      <polygon transform="translate(5,5)" fill="#2b2b2b" points="131,2 148,24 172,8 178,34 206,26 202,52 232,52 218,74 250,82 226,98 250,116 220,122 232,146 202,144 204,166 176,156 166,166 148,150 131,166 114,150 96,166 86,156 58,166 60,144 30,146 42,122 12,116 36,98 12,82 44,74 30,52 60,52 56,26 84,34 90,8 114,24"/>
      <polygon fill="#f37123" points="131,2 148,24 172,8 178,34 206,26 202,52 232,52 218,74 250,82 226,98 250,116 220,122 232,146 202,144 204,166 176,156 166,166 148,150 131,166 114,150 96,166 86,156 58,166 60,144 30,146 42,122 12,116 36,98 12,82 44,74 30,52 60,52 56,26 84,34 90,8 114,24"/>
    </svg>
    <div class="venue__text"><span>Hillcrest Nursing</span><span>Home - Stawell</span><span>9:00am - 3:00pm</span></div>
  </div>

  <h1 class="headline">Double Qualification -<br>Cert III in Aged Care with<br>Home and Community Care</h1>

  <p class="funding">Government Funding for eligible students!<br>Fees from $117</p>

  <section class="enrol">
    <div class="enrol__label">TO ENROL VISIT</div>
    <div class="enrol__web">brightpathlearning.com.au</div>
    <div class="enrol__phone">OR CALL 9555 0142</div>
  </section>

  <section class="modules">
    <div class="modules__inner">
      <p class="modules__intro">This training is delivered with VIC and<br>Comm Govt Funding to<br>eligible students</p>
      <ul class="modules__list">
        <li><svg viewBox="0 0 14 14"><path d="M2 2 L12 12 M12 2 L2 12" stroke="#1a1a1a" stroke-width="2"/></svg>Pathology</li>
        <li><svg viewBox="0 0 14 14"><path d="M2 2 L12 12 M12 2 L2 12" stroke="#1a1a1a" stroke-width="2"/></svg>Aged Care</li>
        <li><svg viewBox="0 0 14 14"><path d="M2 2 L12 12 M12 2 L2 12" stroke="#1a1a1a" stroke-width="2"/></svg>First Aid</li>
        <li><svg viewBox="0 0 14 14"><path d="M2 2 L12 12 M12 2 L2 12" stroke="#1a1a1a" stroke-width="2"/></svg>CPR</li>
        <li><svg viewBox="0 0 14 14"><path d="M2 2 L12 12 M12 2 L2 12" stroke="#1a1a1a" stroke-width="2"/></svg>Anaphylaxis</li>
        <li><svg viewBox="0 0 14 14"><path d="M2 2 L12 12 M12 2 L2 12" stroke="#1a1a1a" stroke-width="2"/></svg>Home &amp; Community Care</li>
        <li><svg viewBox="0 0 14 14"><path d="M2 2 L12 12 M12 2 L2 12" stroke="#1a1a1a" stroke-width="2"/></svg>Medications for PCA’s</li>
        <li><svg viewBox="0 0 14 14"><path d="M2 2 L12 12 M12 2 L2 12" stroke="#1a1a1a" stroke-width="2"/></svg>Health Services</li>
      </ul>
    </div>
  </section>

  <div class="brand">
    <span class="brand__dot"></span>
    <span class="brand__name">Bright Path Learning</span>
  </div>
  <div class="toid">Toid 40518</div>
</body>
</html>
```